WEBSITE DESIGN, VELTRA paint and panel

We are in need of a website for Veltra Paint & Panel based in Brisbane, Australia. We are a boutique Automotive Paint & Panel Company that provides services to all makes and models of vehicles. We have attached a logo that is still in draft stage but gives you an idea of the colour scheme and fonts and overall impact we are looking for. We are after a white background so this is clean and crisp whilst being sleek, modern and professional. The website must represent our slogan of Flawless shade on the Finest frame. The website must therefore be visually effective as our product is to get colour and placement on vehicle body's correct so the website must have this impact on our clients. We are after a widescreen webpage that is simple and logical to navigate. The final design should give clients the confidence that we can deliver on our promise.
Updates

Target Market(s)

Vehicle Owners who have a need for panel repairs and people who want to reinvigorate their car with a new coat of paint.

Industry/Entity Type

Car Repair

Coding

Coded - Design and coding required

Number of Pages Required

5+ page

Font styles to use
Sans Serif

Colors
ffffff
ffc214
000000

Requirements
Must have
• Page 1 - Home Page
• Page 2 - Our Process
• Page 3 - Private Customers
• Page 4 - Fleet & Corporate
• Page 5 - Insurance
• Page 6 - Get a Quote
• Page 7 - Connect (Contacts Page)
• Same font and colour scheme as the logo.
Should not have
• A typical mechanical/paint and panel layout which looks like a template website.

```html
<!DOCTYPE html>
<html lang="en">
<head>
<meta charset="utf-8">
<title>Veltra Paint &amp; Panel</title>
<link href="https://fonts.googleapis.com/css2?family=Open+Sans:wght@400;600;700;800&family=Cinzel:wght@400;700&display=swap" rel="stylesheet">
<style>
:root{
  --yellow:#ffc214;
  --yellow-soft:#ffe07a;
  --black:#000000;
  --ink:#222222;
  --grey-text:#777777;
  --nav-bg:#111111;
  --nav-active:#3a3a3a;
  --light-bg:#ececec;
  --white:#ffffff;
}
*{box-sizing:border-box;margin:0;padding:0}
html,body{width:885px;height:1200px;overflow:hidden;background:var(--white)}
body{font-family:"Open Sans",Arial,sans-serif;color:var(--ink);position:relative}
.wrap{position:absolute;left:106px;width:674px}

/* header */
.site-header{position:absolute;top:0;left:0;width:885px;height:88px}
.brand{position:absolute;left:106px;top:14px;text-align:center}
.brand-name{font-family:"Open Sans",sans-serif;font-weight:800;font-size:34px;letter-spacing:3px;color:var(--black);line-height:1}
.brand-tag{font-size:10px;color:var(--black);letter-spacing:1px;margin-top:3px}
.call{position:absolute;right:105px;top:28px;text-align:right}
.call-label{font-size:10px;color:var(--yellow);font-weight:600}
.call-number{display:flex;align-items:center;gap:5px;font-size:15px;font-weight:700;color:var(--black)}

/* nav */
.main-nav{position:absolute;top:88px;left:0;width:885px;height:30px;background:var(--yellow)}
.main-nav ul{position:absolute;left:106px;width:674px;height:30px;list-style:none;display:flex;background:var(--nav-bg)}
.main-nav li{font-size:10.5px;color:var(--white);padding:0 13px;line-height:30px}
.main-nav li.active{background:var(--nav-active)}

/* hero */
.hero{position:absolute;top:118px;left:0;width:885px;height:348px;overflow:hidden}
.hero-photo{position:absolute;inset:0;background:linear-gradient(120deg,#6b89ad 0%,#9fb6cf 40%,#3f5f87 70%,#273b57 100%)}
.hero svg{position:absolute;inset:0}
.hero-title{position:absolute;left:106px;top:145px;font-family:"Cinzel",serif;color:var(--ink)}
.hero-title .small{font-size:14px;letter-spacing:.5px}
.hero-title .big{font-size:28px;line-height:1.15}

/* intro */
.intro{top:492px;text-align:center}
.intro h1{font-size:20px;font-weight:600;color:var(--ink)}
.intro h2{font-size:12px;font-weight:400;color:var(--grey-text);margin-top:4px}
.intro p{font-size:8px;color:var(--grey-text);line-height:1.6;margin:14px 40px 0}

/* services */
.services{top:615px;height:170px}
.service{position:absolute;top:0;width:170px;height:170px;border-radius:50%;border:3px solid var(--yellow);padding:42px 18px 0 22px}
.service:nth-child(1){left:45px}
.service:nth-child(2){left:252px}
.service:nth-child(3){left:459px}
.service-head{display:flex;gap:8px;align-items:flex-start}
.service-head svg{flex:none;margin-top:2px}
.service h3{font-size:11px;font-weight:700;color:var(--ink);line-height:1.2}
.service p{font-size:7px;color:var(--grey-text);line-height:1.5;margin:6px 0 0 40px}
.service .more{font-size:7px;font-weight:700;color:var(--yellow);margin:5px 0 0 40px}

/* highlights */
.highlights-band{position:absolute;top:826px;left:0;width:885px;height:270px;background:var(--light-bg)}
.cards{top:860px;display:flex;gap:19px}
.card{width:212px;height:200px;background:var(--white)}
.card-photo{height:112px}
.card-photo.process{background:linear-gradient(135deg,#b9b3aa,#6d6a66)}
.card-photo.painting{background:linear-gradient(135deg,#8a7a5c,#3e3a33)}
.card-photo.private{background:linear-gradient(135deg,#c7323a,#d9dde3)}
.card h4{font-size:13px;font-weight:600;color:var(--ink);margin:14px 12px 0}
.card p{font-size:7px;color:var(--grey-text);line-height:1.5;margin:5px 12px 0}

/* footer */
.site-footer{position:absolute;top:1097px;left:0;width:885px;height:103px;background:var(--black)}
.footer-links{position:absolute;left:106px;top:22px;font-size:9px;color:var(--white)}
.footer-links span{margin-right:6px}
.copyright{position:absolute;left:106px;top:42px;font-size:7px;color:#888}
.social{position:absolute;left:708px;top:20px;display:flex;gap:4px}
.social span{width:18px;height:18px;border-radius:50%;display:block}
.social span:nth-child(1),.social span:nth-child(2){background:#3b8fd4}
.social span:nth-child(3),.social span:nth-child(4){background:#d23b30}
</style>
</head>
<body>

<header class="site-header">
  <div class="brand">
    <div class="brand-name">VELTRA</div>
    <div class="brand-tag">paint and panel</div>
  </div>
  <div class="call">
    <div class="call-label">Call us Now</div>
    <div class="call-number">
      <svg width="14" height="14" viewBox="0 0 24 24"><circle cx="12" cy="12" r="12" fill="#000"/><path d="M8 6.5c.5-.5 1.2-.4 1.5.1l1.2 2c.3.5.2 1-.2 1.3l-.8.6c.6 1.4 1.7 2.5 3.1 3.1l.6-.8c.3-.4.9-.5 1.3-.2l2 1.2c.5.3.6 1 .1 1.5l-1 1c-3.5.4-8.2-4.3-7.8-7.8z" fill="#fff"/></svg>
      555 201 7730
    </div>
  </div>
</header>

<nav class="main-nav">
  <ul>
    <li class="active">Home</li>
    <li>Our Process</li>
    <li>Private Customers</li>
    <li>Fleet &amp; Corporate Insurance</li>
    <li>Get a Quote</li>
    <li>Contact</li>
  </ul>
</nav>

<section class="hero">
  <div class="hero-photo" role="img" aria-label="Painter in protective mask spraying a car body panel in a paint booth"></div>
  <svg width="885" height="348" viewBox="0 0 885 348" aria-hidden="true">
    <polygon points="0,0 580,0 390,348 0,348" fill="#ffc214"/>
    <polygon points="0,110 470,40 380,230 0,290" fill="#ffe07a" opacity=".55"/>
  </svg>
  <div class="hero-title">
    <div class="small">FLAWLESS SHADE ON THE</div>
    <div class="big">FINEST FRAME</div>
  </div>
</section>

<section class="wrap intro">
  <h1>Morbi libero ullamcorper nonummy nibh</h1>
  <h2>metus eget consectetuer augue nisi quis</h2>
  <p>Lorem ipsum dolor sit amet consectetur adipiscing elit sed do eiusmod tempor incididunt ut labore et dolore magna aliqua. Ut enim ad minim veniam quis nostrud exercitation ullamco laboris nisi ut aliquip ex ea commodo consequat. Duis aute irure dolor in reprehenderit in voluptate velit esse cillum dolore.</p>
</section>

<section class="wrap services">
  <div class="service">
    <div class="service-head">
      <svg width="32" height="22" viewBox="0 0 32 22"><path d="M3 14l3-7h14l6 5h3v5H3z" fill="none" stroke="#222" stroke-width="2"/><circle cx="9" cy="17" r="3" fill="#222"/><circle cx="24" cy="17" r="3" fill="#222"/></svg>
      <h3>VEHICLES<br>PAINT</h3>
    </div>
    <p>Lorem ipsum dolor sit amet consectetuer adipiscing elit sed diam</p>
    <div class="more">LEARN MORE &rsaquo;</div>
  </div>
  <div class="service">
    <div class="service-head">
      <svg width="32" height="22" viewBox="0 0 32 22"><path d="M2 15l4-8h18l6 6v4H2z" fill="#222"/><circle cx="9" cy="17" r="3" fill="#fff" stroke="#222" stroke-width="2"/><circle cx="24" cy="17" r="3" fill="#fff" stroke="#222" stroke-width="2"/></svg>
      <h3>NEW COAT<br>COLORS</h3>
    </div>
    <p>Lorem ipsum dolor sit amet consectetuer adipiscing elit sed diam</p>
    <div class="more">LEARN MORE &rsaquo;</div>
  </div>
  <div class="service">
    <div class="service-head">
      <svg width="32" height="24" viewBox="0 0 32 24"><path d="M3 3h18v12H10l-5 4v-4H3z" fill="none" stroke="#222" stroke-width="2"/><path d="M13 9h16v10h-2v3l-4-3h-10z" fill="#222"/></svg>
      <h3>GET A QUOTE<br>NOW</h3>
    </div>
    <p>Lorem ipsum dolor sit amet consectetuer adipiscing elit sed diam</p>
    <div class="more">LEARN MORE &rsaquo;</div>
  </div>
</section>

<div class="highlights-band"></div>
<section class="wrap cards">
  <article class="card">
    <div class="card-photo process" role="img" aria-label="Workshop bay with cars being prepared for painting"></div>
    <h4>Our Process</h4>
    <p>Lorem ipsum dolor sit amet consectetuer adipiscing elit sed diam nonummy nibh euismod tincidunt ut laoreet</p>
  </article>
  <article class="card">
    <div class="card-photo painting" role="img" aria-label="Technician spray painting a car panel"></div>
    <h4>How we Paint Car</h4>
    <p>Lorem ipsum dolor sit amet consectetuer adipiscing elit sed diam nonummy nibh euismod tincidunt ut laoreet</p>
  </article>
  <article class="card">
    <div class="card-photo private" role="img" aria-label="Freshly painted red car in a garage"></div>
    <h4>Private Customers</h4>
    <p>Lorem ipsum dolor sit amet consectetuer adipiscing elit sed diam nonummy nibh euismod tincidunt ut laoreet</p>
  </article>
</section>

<footer class="site-footer">
  <div class="footer-links">
    <span>Home</span>|<span> Our Process</span>|<span> Private Customers</span>|<span> Fleet &amp; Corporate Insurance</span>|<span> Get a Quote</span>|<span> Contact</span>
  </div>
  <div class="copyright">&copy; 2015 Company Name. All rights reserved. Terms of Use</div>
  <div class="social" aria-label="Social links"><span></span><span></span><span></span><span></span></div>
</footer>

</body>
</html>
```